Exterior cleaning company requires a eye catching a5 leaflet

we need some updated leaflet designs, a5 folded, we are targeting all exterior cleaning contracts, including roof cleaning & treatment, render cleaning & Treatment, driveways, block paving cleaning using the latest in low pressure cleaning technologies along side high pressure jetwashing. gutter clearance and flushing, water fed telescopic pole window cleaning of difficult to reach windows and high buildings. our website : www.tkbellowsec.co.uk facebook page: https://www.facebook.com/tkbellowsexteriorcareltd Instagram: https://www.instagram.com/tkbellowsec/ a quick google search of roof cleaning, soft washing etc will provide results of what we are doing

Target Market(s)

home owners, commercial clients

Font styles to use
Serif
Sans Serif

Requirements
Must have
• A5 Landscape folded leaflet, front page with company information and bullet points of main works : window & conservatory cleaning, roof cleaning & treatment, Render cleaning & treatment, pressure washing, soft washing, gutter clearing, pressure washing of patios, driveways, gutters, fascias (more info can be provided on techniques etc if required)

```html
<!DOCTYPE html>
<html lang="en">
<head>
<meta charset="utf-8">
<title>TK Bellows Exterior Care – A5 Leaflet Front</title>
<link rel="stylesheet" href="https://fonts.googleapis.com/css2?family=Montserrat:wght@300;400;500;600;700;800&display=swap">
<style>
  :root{
    --bg:#d9d9dc;
    --paper:#ffffff;
    --paper-shade:#eeeeef;
    --charcoal:#2b2b2b;
    --ink:#111111;
    --muted:#6a6a6a;
    --rule:#9a9a9a;
    --accent:#2a8fd6;
  }
  *{box-sizing:border-box;margin:0;padding:0}
  html,body{width:1200px;height:840px;overflow:hidden}
  body{background:var(--bg);font-family:"Montserrat",Arial,sans-serif;color:var(--ink)}
  .leaflet{
    position:absolute;left:320px;top:23px;width:560px;height:794px;
    background:linear-gradient(180deg,var(--paper) 55%,var(--paper-shade) 100%);
    box-shadow:0 10px 30px rgba(0,0,0,.18);overflow:hidden;
  }
  .leaflet__shapes{position:absolute;inset:0}
  .brand-title{position:absolute;left:38px;top:48px;color:#fff}
  .brand-title__name{display:block;font-weight:800;font-size:46px;letter-spacing:1px;line-height:1}
  .brand-title__line{display:block;font-weight:400;font-size:31px;letter-spacing:3px;margin-top:8px}
  .services{position:absolute;left:34px;top:478px;list-style:none}
  .services li{font-weight:500;font-size:19px;line-height:27px;white-space:nowrap}
  .services .mark{font-weight:800;margin-right:6px}
  .services .gap{display:inline-block;width:22px}
  .experience{
    position:absolute;left:34px;top:708px;width:262px;height:34px;
    background:var(--ink);color:#fff;font-weight:700;font-size:14px;
    letter-spacing:.5px;display:flex;align-items:center;justify-content:center;
    clip-path:polygon(0 0,94% 0,100% 50%,94% 100%,0 100%);
  }
  .website{position:absolute;left:34px;top:756px;font-size:17px;font-weight:300;color:#333;letter-spacing:.3px}
  .website b{font-weight:600}
  .contact-card{
    position:absolute;left:320px;top:664px;width:222px;height:82px;
    display:flex;align-items:center;gap:12px;
  }
  .contact-card__mark{width:54px;height:54px;border:1.5px solid var(--ink);border-radius:50%;flex:none}
  .contact-card__name{font-weight:700;font-size:15px;line-height:18px}
  .contact-card__tel{font-weight:700;font-size:12px;margin-top:4px}
</style>
</head>
<body>
  <main class="leaflet">
    <svg class="leaflet__shapes" width="560" height="794" viewBox="0 0 560 794">
      <defs>
        <linearGradient id="photoTone" x1="0" y1="1" x2="1" y2="0">
          <stop offset="0" stop-color="#b69a7c"/>
          <stop offset=".35" stop-color="#5d6b4b"/>
          <stop offset=".65" stop-color="#4a5258"/>
          <stop offset="1" stop-color="#8a5a3e"/>
        </linearGradient>
      </defs>
      <rect class="header-band" x="0" y="0" width="560" height="300" fill="var(--charcoal)"/>
      <polygon class="header-band__cut" points="0,300 560,300 560,330 0,330" fill="var(--paper)"/>
      <polygon class="hero-photo" role="img" aria-label="Photo of a cleaner using a water-fed pole on the glass walls of a modern conservatory beside a stone patio"
               points="0,205 560,120 560,300 330,460 0,460" fill="url(#photoTone)"/>
      <line x1="300" y1="640" x2="545" y2="640" stroke="var(--rule)" stroke-width="1"/>
      <line x1="34" y1="748" x2="545" y2="748" stroke="var(--rule)" stroke-width="1"/>
    </svg>

    <h1 class="brand-title">
      <span class="brand-title__name">TK BELLOWS</span>
      <span class="brand-title__line">EXTERIOR CARE</span>
    </h1>

    <ul class="services">
      <li><span class="mark">»</span>Window &amp; Conservatory Cleaning</li>
      <li><span class="mark">»</span>Roof Cleaning &amp; Treatment</li>
      <li><span class="mark">»</span>Render Cleaning &amp; Treatment</li>
      <li><span class="mark">»</span>Pressure Washing<span class="gap"></span><span class="mark">»</span>Soft Washing</li>
      <li><span class="mark">»</span>Gutter Clearing</li>
      <li><span class="mark">»</span>Pressure Washing Of Patios</li>
      <li><span class="mark">»</span>Driveways<span class="gap"></span><span class="mark">»</span>Gutters<span class="gap"></span><span class="mark">»</span>Fascias</li>
    </ul>

    <div class="experience">OVER 10 YEARS EXPERIENCE</div>
    <p class="website">www.<b>tkbellowsec</b>.co.uk</p>

    <div class="contact-card">
      <span class="contact-card__mark"></span>
      <div>
        <p class="contact-card__name">TK Bellows Exterior Care Ltd</p>
        <p class="contact-card__tel">Tel: 01632 960 418</p>
      </div>
    </div>
  </main>
</body>
</html>
```